Bright Tooth Dentistry Business Card

We need business cards for our dental office.
We are looking for a clean, elegant design

We provide dental services to children.
Our card needs to be appealing to referring dentists, parents and our team

Target Market(s)

referring dentists, parents and our team

Industry/Entity Type

Dental Clinic

Contact Information for Business Card

4816 Juniper Lane, Suite 100
Middleburg Heights, OH 15237

412-837-2961 Voice
412-837-2962 fax
info@brighttoothdentalpa.com email
www.brighttoothdentalpa.com web

Font styles to use
Sans Serif

Requirements
Must have
• White background - clean, crisp, elegant, simple
• rounded corners
• different color palate - once we come up with design, we will replace the blue with orange, green,
Nice to have
• Follow our logo typeface and colors
• then we can replace color

```html
<!DOCTYPE html>
<html lang="en">
<head>
<meta charset="utf-8">
<title>Bright Tooth Dentistry – Business Card</title>
<link href="https://fonts.googleapis.com/css2?family=Quicksand:wght@500&family=Arimo:wght@400&display=swap" rel="stylesheet">
<style>
  :root {
    --stage: #5c5c5c;
    --brand-blue: #00aeef;
    --brand-grey: #a7a9ac;
    --grey-light: #c4c6c8;
    --faint-grey: #f2f2f2;
    --card-white: #ffffff;
    --text-white: #ffffff;
  }
  html, body {
    margin: 0;
    padding: 0;
    width: 1200px;
    height: 802px;
    overflow: hidden;
    background: var(--stage);
  }
  .stage {
    position: relative;
    width: 1200px;
    height: 802px;
  }
  .card {
    position: absolute;
    top: 274px;
    width: 443px;
    height: 265px;
    overflow: hidden;
    box-shadow: 0 3px 6px rgba(0,0,0,0.45);
  }
  .card--contact {
    left: 136px;
    background: var(--brand-blue);
  }
  .card--brand {
    left: 624px;
    background: var(--card-white);
  }
  .contact-art {
    position: absolute;
    left: 0;
    top: 0;
    width: 443px;
    height: 265px;
  }
  .contact-list {
    position: absolute;
    right: 31px;
    top: 132px;
    margin: 0;
    padding: 0;
    list-style: none;
    font-family: "Arimo", Arial, sans-serif;
    font-size: 12.5px;
    color: var(--text-white);
    text-align: right;
  }
  .contact-list li {
    display: flex;
    justify-content: flex-end;
    align-items: center;
    gap: 3px;
    height: 16px;
  }
  .contact-list .gap-before {
    margin-top: 12px;
  }
  .contact-list .address-block {
    align-items: flex-start;
    gap: 4px;
    height: auto;
    line-height: 16px;
  }
  .icon {
    width: 11px;
    height: 11px;
    flex: none;
    fill: var(--text-white);
  }
  .address-block .icon {
    margin-top: 2px;
  }
  .brand-backdrop {
    position: absolute;
    left: 0;
    top: 0;
    width: 215px;
    height: 245px;
    background: radial-gradient(ellipse at 55% 35%, var(--faint-grey) 0%, rgba(242,242,242,0.6) 45%, rgba(255,255,255,0) 75%);
  }
  .brand-name {
    position: absolute;
    left: 0;
    right: 0;
    top: 146px;
    text-align: center;
    font-family: "Quicksand", sans-serif;
    font-weight: 500;
    font-size: 31px;
    line-height: 40px;
    color: var(--brand-blue);
    display: flex;
    justify-content: center;
    align-items: center;
    gap: 8px;
  }
  .brand-dot {
    width: 12px;
    height: 12px;
    border-radius: 50%;
    background: var(--brand-grey);
  }
</style>
</head>
<body>
<main class="stage">
  <section class="card card--contact">
    <svg class="contact-art" viewBox="0 0 443 265" role="img" aria-label="Large tooth outline with sparkles decoration">
      <defs>
        <linearGradient id="art-fill" x1="0" y1="0" x2="1" y2="0.4">
          <stop offset="0" stop-color="var(--brand-grey)"/>
          <stop offset="0.6" stop-color="var(--grey-light)"/>
          <stop offset="1" stop-color="var(--brand-grey)"/>
        </linearGradient>
      </defs>
      <path d="M0 0 H234 C256 40 266 62 242 110 C210 165 178 215 150 265 H0 Z" fill="url(#art-fill)"/>
    </svg>
    <ul class="contact-list">
      <li>412-837-2961
        <svg class="icon" viewBox="0 0 12 12"><path d="M1 4 C1 1.5 11 1.5 11 4 V5 H8.5 V3.8 H3.5 V5 H1 Z M3 6 H9 L10.5 10.5 H1.5 Z"/></svg>
      </li>
      <li>412-837-2962
        <svg class="icon" viewBox="0 0 12 12"><path d="M3 1 H9 V4 H3 Z M1 4.5 H11 V9 H9 V11 H3 V9 H1 Z M4 7.5 V10 H8 V7.5 Z"/></svg>
      </li>
      <li>info@brighttoothdentalpa.com
        <svg class="icon" viewBox="0 0 12 12"><path d="M0.5 2.5 H11.5 V9.5 H0.5 Z" fill="none" stroke="#fff"/><path d="M0.5 2.5 L6 7 L11.5 2.5" fill="none" stroke="#fff"/></svg>
      </li>
      <li>www.brighttoothdentalpa.com
        <svg class="icon" viewBox="0 0 12 12"><circle cx="6" cy="6" r="5.5"/><path d="M3 4 L5 3.5 L6 5 L4.5 7 Z M7 7 L9 6.5 L8.5 9 Z" fill="var(--brand-blue)"/></svg>
      </li>
      <li class="address-block gap-before">
        <span>4816 Juniper Lane, Suite 100<br>Middleburg Heights, OH 15237</span>
        <svg class="icon" viewBox="0 0 12 12"><path d="M6 0.5 C3.5 0.5 2 2.3 2 4.3 C2 7 6 11.5 6 11.5 C6 11.5 10 7 10 4.3 C10 2.3 8.5 0.5 6 0.5 Z M6 2.8 A1.5 1.5 0 1 0 6.01 2.8 Z" fill-rule="evenodd"/></svg>
      </li>
    </ul>
  </section>

  <section class="card card--brand">
    <div class="brand-backdrop" role="img" aria-label="Faint tooth and sparkles decoration"></div>
    <div class="brand-name"><span class="brand-dot"></span>Bright Tooth Dentistry</div>
  </section>
</main>
</body>
</html>
```